https://www.lernwinkel.de - a website for school website in germany for presentation/paper download

we own the webpage https://www.lernwinkel.de and we need a new webdesign (a new website logo is also possible). we want only new images and css, we don´t want to made any change to the HTML code.
we need only new images/color for a new modern look.

we want to have more trust to our user. they have to download presentation/paper
we need template for this sites:
https://www.lernwinkel.de/
https://www.lernwinkel.de/referate/englisch
https://www.lernwinkel.de/forum.php
https://www.lernwinkel.de/forum/insektenhotel/258614
https://www.lernwinkel.de/referat/latein/sokrates/25892
https://www.lernwinkel.de/schule_seminararbeit_fachliste.php?fach=238
and other sites on the website. (take a look around the website)

we don´t like white color for sublines or text. (h1/h2/strong) . in image are white Text OK.

important: we want to chance ONLY the CSS and PICS, we don´t want to remove or chance any HTML code.

after you have made a mockup of the new design and we give you a go, you have to made a package with the IMAGES and the CSS rules (text how we have to chance the current css)

Target Market(s)

Germany, Austria, Switzerland -DACH

Industry/Entity Type

School

Coding

Coded - Design and coding required

Number of Pages Required

5+ page

Font styles to use
Serif
Sans Serif

Colors

Designer to choose colors to be used in the design.

Requirements
Must have
• We want only to remove images and no HTML Code
Should not have
• NO white colors for Text on the site. In images are OK

```html
<!DOCTYPE html>
<html lang="de">
<head>
<meta charset="utf-8">
<title>Lernwinkel.de – Referate, Hausaufgaben und nette Leute kennenlernen</title>
<link rel="stylesheet" href="https://fonts.googleapis.com/css2?family=Roboto+Slab:wght@400;500&family=Roboto:wght@400;500;700&display=swap">
<style>
:root{
  --navy:#2b2f4d;
  --teal:#45afac;
  --red:#e0504a;
  --grey:#efefef;
  --line:#dcdcdc;
  --text:#333;
  --muted:#666;
  --white:#fff;
  --backdrop-a:#c9c6c2;
  --backdrop-b:#e4e2df;
}
*{box-sizing:border-box;margin:0;padding:0}
html,body{width:1200px;height:842px;overflow:hidden}
body{
  font-family:"Roboto",Arial,sans-serif;font-size:12px;color:var(--text);
  position:relative;
}
.backdrop{position:absolute;inset:0;background:linear-gradient(90deg,var(--backdrop-a),var(--backdrop-b) 30%,var(--backdrop-b) 70%,var(--backdrop-a))}
.page{position:absolute;left:161px;top:0;width:878px;height:842px;background:var(--white)}
.slab{font-family:"Roboto Slab",Georgia,serif}
a{color:inherit;text-decoration:none}

/* header */
.site-header{position:absolute;left:11px;top:0;width:856px;height:96px;background:var(--navy);overflow:hidden}
.header-photo{position:absolute;right:0;top:0;width:420px;height:96px;background:linear-gradient(90deg,var(--navy),#3a3d55 40%,#5a4a45 75%,#7a2f2c)}
.brand{position:absolute;left:26px;top:30px;display:flex;align-items:center;gap:9px;color:var(--white);font-family:"Roboto Slab",Georgia,serif;font-size:25px}
.brand-dot{width:14px;height:14px;border-radius:50%;background:var(--teal)}
.tagline{position:absolute;left:26px;top:66px;color:var(--white);font-size:7px;letter-spacing:.2px}
.login{position:absolute;left:481px;top:51px;width:366px;height:33px;background:var(--white);border-radius:17px;display:flex;align-items:center;padding:0 10px;font-family:"Roboto Slab",Georgia,serif;font-size:11.5px;color:var(--text)}
.login input{width:75px;height:14px;border:1px solid #ccc;border-radius:8px;margin:0 10px 0 6px}
.login input.pw{width:86px}
.login button{background:var(--red);color:var(--white);border:0;border-radius:8px;font:inherit;font-size:10px;padding:2px 10px}

/* nav */
.main-nav{position:absolute;left:11px;top:99px;width:856px;height:23px;background:var(--grey);display:flex;font-family:"Roboto Slab",Georgia,serif;font-size:11.5px}
.main-nav a{display:flex;align-items:center;gap:6px;padding:0 10px;border-right:1px solid var(--line);color:var(--text)}
.main-nav svg{width:12px;height:12px;fill:var(--teal)}
.sub-nav{position:absolute;left:11px;top:126px;width:856px;height:22px;background:var(--red);display:flex;align-items:center;font-family:"Roboto Slab",Georgia,serif;font-size:11.5px;color:var(--white);padding-left:12px}
.sub-nav span.sep{margin:0 26px}

/* columns */
.col-left{position:absolute;left:11px;top:154px;width:207px}
.col-main{position:absolute;left:222px;top:154px;width:507px}
.col-right{position:absolute;left:733px;top:154px;width:134px}

.box-head{height:25px;display:flex;align-items:center;gap:8px;padding-left:10px;color:var(--white);font-family:"Roboto Slab",Georgia,serif;font-size:13px;font-weight:500}
.box-head svg{width:12px;height:12px;fill:var(--white)}
.teal{background:var(--teal)}
.redbg{background:var(--red)}
.navybg{background:var(--navy)}
.menu{list-style:none;margin-bottom:4px}
.menu li{height:24px;display:flex;align-items:center;justify-content:space-between;padding:0 24px 0 16px;background:var(--grey);border-bottom:1px solid var(--white);font-family:"Roboto Slab",Georgia,serif;font-size:11.5px}
.menu svg{width:6px;height:8px;stroke:var(--text);fill:none;stroke-width:1.4}
.stats li{padding-right:26px}
.new-member{border:1px solid var(--line);border-top:0;height:166px;padding:10px 10px}
.avatar{width:86px;height:85px;background:#4a90c8}
.member-name{margin-top:12px;font-family:"Roboto Slab",Georgia,serif;font-size:13px;display:flex;align-items:center;gap:4px;padding-left:4px}
.member-name svg{width:11px;height:11px;stroke:var(--teal);fill:none;stroke-width:1.6}
.member-age{color:var(--muted);font-size:11.5px;padding-left:4px;margin-top:3px}
.member-link{color:var(--red);font-family:"Roboto Slab",Georgia,serif;font-size:11.5px;padding-left:4px;margin-top:3px}

.intro{border:1px solid var(--line);height:224px;position:relative;overflow:hidden}
.search{position:absolute;left:9px;top:7px;width:488px;height:41px;background:var(--navy);display:flex;align-items:center;padding-left:12px;color:var(--white);font-family:"Roboto Slab",Georgia,serif;font-size:11.5px}
.search input{width:323px;height:17px;border:0;border-radius:9px;margin:0 10px 0 6px;padding-left:7px;font-size:9px;font-family:"Roboto",sans-serif;color:var(--muted)}
.search button{background:var(--red);color:var(--white);border:0;border-radius:9px;font:inherit;font-size:10px;padding:2px 17px}
.intro-art{position:absolute;right:0;top:58px;width:185px;height:166px;background:linear-gradient(135deg,#f3f3f3,#dfe2e8 60%,#e9c46a)}
.intro-text{position:absolute;left:16px;top:68px;width:330px;color:var(--muted);font-size:11.5px;line-height:18.7px}
.intro-text .hl{color:var(--red);font-weight:700}
.intro-text .tl{color:var(--teal);font-weight:700}
.intro-text p{margin-bottom:12px}
.subjects{margin-top:6px;border:1px solid var(--line);background:var(--grey);height:153px}
.subjects .box-head{background:var(--navy);height:24px;padding-left:16px;font-weight:400}
.subjects p{padding:9px 14px 0 16px;line-height:21px;font-size:11.5px;color:var(--text)}
.subjects b{color:var(--teal);font-weight:700}

.messenger{border:1px solid var(--line);border-top:0;height:66px;text-align:center;font-size:10.5px;line-height:15px;padding-top:8px;font-family:"Roboto Slab",Georgia,serif}
.messenger .links{margin-top:4px;font-size:11.5px;color:var(--red)}
.messenger .links span{color:var(--text)}
.side-bar{height:21px;display:flex;align-items:center;justify-content:center;color:var(--white);font-family:"Roboto Slab",Georgia,serif;font-size:11.5px}
.promo{position:relative;height:167px;background:linear-gradient(160deg,#dfe3ea,#f2efe9 55%,#e7e2da);overflow:hidden}
.promo h3{position:absolute;left:0;right:0;top:104px;text-align:center;font-family:"Roboto",Arial,sans-serif;font-weight:700;font-size:18px;color:var(--navy)}
.promo a{position:absolute;left:5px;right:5px;top:133px;height:23px;border-radius:12px;background:var(--red);color:var(--white);font-size:11px;font-weight:500;display:flex;align-items:center;justify-content:center}

.site-footer{position:absolute;left:0;top:769px;width:878px;height:73px;background:var(--navy);color:var(--white);font-family:"Roboto Slab",Georgia,serif;font-size:11.5px;display:flex;align-items:center;justify-content:center;padding-bottom:6px}
</style>
</head>
<body>
<div class="backdrop" role="img" aria-label="Blurred library bookshelves background"></div>
<div class="page">
  <header class="site-header">
    <div class="header-photo" role="img" aria-label="Stack of books with a red apple"></div>
    <a class="brand" href="https://www.lernwinkel.de/"><span class="brand-dot"></span>Lernwinkel.de</a>
    <div class="tagline">Referate, Hausaufgaben und nette Leute kennenlernen</div>
    <form class="login">Nick name<input type="text">Passwort<input class="pw" type="password"><button type="button">Login</button></form>
  </header>

  <nav class="main-nav">
    <a href="https://www.lernwinkel.de/"><svg viewBox="0 0 12 12"><path d="M6 1 0 6h2v5h3V8h2v3h3V6h2z"/></svg>Startseite</a>
    <a href="https://www.lernwinkel.de/forum.php"><svg viewBox="0 0 12 12"><circle cx="4" cy="3.5" r="2"/><circle cx="8.5" cy="4" r="1.7"/><path d="M0 10c0-3 2-4 4-4s4 1 4 4zM8 6.5c2 0 4 1 4 3.5H9c0-1.5-.3-2.5-1-3.5z"/></svg>Community</a>
    <a href="https://www.lernwinkel.de/referate/englisch"><svg viewBox="0 0 12 12"><path d="M6 0 0 3v1h12V3zM1 5h2v4H1zm4 0h2v4H5zm4 0h2v4H9zM0 10h12v2H0z"/></svg>Referate</a>
  </nav>
  <nav class="sub-nav"><span>Foren</span><span class="sep">|</span><span>Mitglieder</span><span class="sep">|</span><span>Flirtsuche</span></nav>

  <aside class="col-left">
    <div class="box-head teal"><svg viewBox="0 0 12 12"><circle cx="4" cy="3.5" r="2"/><circle cx="8.5" cy="4" r="1.7"/><path d="M0 10c0-3 2-4 4-4s4 1 4 4zM8 6.5c2 0 4 1 4 3.5H9c0-1.5-.3-2.5-1-3.5z"/></svg>Community</div>
    <ul class="menu">
      <li>Registrieren<svg viewBox="0 0 6 8"><path d="M1 1l3 3-3 3"/></svg></li>
      <li>Mitglieder Login<svg viewBox="0 0 6 8"><path d="M1 1l3 3-3 3"/></svg></li>
      <li>Chat<svg viewBox="0 0 6 8"><path d="M1 1l3 3-3 3"/></svg></li>
      <li>Flirtsuche<svg viewBox="0 0 6 8"><path d="M1 1l3 3-3 3"/></svg></li>
      <li>Forum<svg viewBox="0 0 6 8"><path d="M1 1l3 3-3 3"/></svg></li>
    </ul>
    <div class="box-head teal"><svg viewBox="0 0 12 12"><path d="M6 0 0 3v1h12V3zM1 5h2v4H1zm4 0h2v4H5zm4 0h2v4H9zM0 10h12v2H0z"/></svg>Schule &amp; Uni</div>
    <ul class="menu"><li>Referate / Hausarbeiten<svg viewBox="0 0 6 8"><path d="M1 1l3 3-3 3"/></svg></li></ul>
    <div class="box-head teal"><svg viewBox="0 0 12 12"><path d="M6 0a6 6 0 1 0 0 12A6 6 0 0 0 6 0zm.8 9.5H5.2V5h1.6zM6 4a1 1 0 1 1 0-2 1 1 0 0 1 0 2z"/></svg>Informationem</div>
    <ul class="menu"><li>FAQ<svg viewBox="0 0 6 8"><path d="M1 1l3 3-3 3"/></svg></li></ul>
    <div class="box-head teal"><svg viewBox="0 0 12 12"><path d="M0 11h12v1H0zM1 7h2v3H1zm3-2h2v5H4zm3-2h2v7H7zm3-3h2v10h-2z"/></svg>Statistik</div>
    <ul class="menu stats">
      <li>Mitglieder<span>401.325</span></li>
      <li>Männer<span>197.695</span></li>
      <li>Frauen<span>196.799</span></li>
      <li>Referate<span>12.458</span></li>
      <li>Forenbeiträge<span>3.080.848</span></li>
    </ul>
    <div class="box-head redbg"><svg viewBox="0 0 12 12"><circle cx="7" cy="3.5" r="2.3"/><path d="M2.5 11c0-3 2-4.5 4.5-4.5s4.5 1.5 4.5 4.5zM0 4h1.2V2.8h1V4h1.2v1H2.2v1.2h-1V5H0z"/></svg>Neue Matglieder</div>
    <div class="new-member">
      <div class="avatar" role="img" aria-label="Placeholder profile picture, no photo uploaded"></div>
      <div class="member-name">Tomvik<svg viewBox="0 0 11 11"><circle cx="4.5" cy="6.5" r="3"/><path d="M6.7 4.3 10 1M7 1h3v3"/></svg></div>
      <div class="member-age">Age: 31 years</div>
      <div class="member-link">Profile</div>
    </div>
  </aside>

  <main class="col-main">
    <section class="intro">
      <form class="search">Suchbegriff :<input type="text" placeholder="Was suchst du? Heir eingeben!"><button type="button">Search</button></form>
      <div class="intro-art" role="img" aria-label="Graduation cap resting on a stack of books"></div>
      <div class="intro-text">
        <p>Hallo <span class="hl">Besucher</span>,</p>
        <p>Auf Lernwinkel.de findest du viele <span class="tl">Referate</span>, Facharbeiten und Hausaufgaben. Solltest du einmal ein Referat zu einem Thema nicht finden, kannst du deine Frage bei uns im <span class="tl">Forum</span> stellen, wo dir in der Regel schnell geholfen wird.</p>
        <p>Es sind bereits <span class="hl">401325 Mitglieder</span> bei uns registriert!</p>
      </div>
    </section>
    <section class="subjects">
      <h2 class="box-head">Referate - Hausarbeiten - Hausaufgaben zu folgenden Fächern:</h2>
      <p><b>Deutsch</b> (2937) | <b>Englisch</b> (1113) | <b>Latein</b> (275) | <b>Franzoesisch</b> (196) | <b>Italienisch</b> (32) | <b>Griechisch</b> (28) | <b>Spanisch</b> (74) | <b>Mathematik</b> (99) | <b>Physik</b> (481) | <b>Chemie</b> (450) | <b>Astronomie</b> (82) | <b>Geographie</b> (785) | <b>Geschichte</b> (1870) | <b>Sozialkunde</b> (555) | <b>Wirtschaft</b> (435) | <b>Recht</b> (109) | <b>Musik</b> (448) | <b>Kunst</b> (265) | <b>Religion</b> (521) | <b>Informatik</b> (191) | <b>Stenographie</b> (6) | <b>Hauswirtschaft</b> (109) | <b>Sport</b> (136) | <b>Chor</b> (19) | <b>Orchester</b> (5) | <b>Biologie</b> (1237) |</p>
    </section>
  </main>

  <aside class="col-right">
    <div class="box-head teal"><svg viewBox="0 0 12 12"><path d="M0 0h9v7H3L0 10zM10 3h2v9l-3-2H4V8h6z"/></svg>Live Messenger</div>
    <div class="messenger">Diese Funktion ist nur für<br>Mitglieder verfügbar.<div class="links">Anmelden <span>|</span> Login</div></div>
    <div class="side-bar navybg">Keine neue Nachricht</div>
    <div class="box-head teal" style="margin-top:4px;padding-left:11px">Dein Lernwinkel.de</div>
    <div class="promo" role="img" aria-label="Hand writing on paper with a pencil">
      <h3>Schol dabei?</h3>
      <a href="https://www.lernwinkel.de/">Kostenlos registrieren</a>
    </div>
    <div class="side-bar navybg" style="margin-top:4px;height:24px">193 Mitglieder online</div>
  </aside>

  <footer class="site-footer">Home | Department of School - Housework | imprint | data protection | Conditions</footer>
</div>
</body>
</html>
```